Business Card design for a skin clinic

i would like a business card design for our skin clinic.
our logo colors are Blue and Grey and Bule /white.
we are searching for a minimalistic design yet very elegant,dynamic and professional which can reflect a professional medical skin care clinic( not a beauty salon).
THE DESGIN IS NOT FOR A PERSON IT WILL BE USED IN THE CLINIC FOR CLIENTS SO THERE SHOULD BE NO NAME OF A PERSON ONLY THE CLINIC NAME AND THE CONTACT INFO

Target Market(s)
young and old womens
Industry/Entity Type
Business
Contact Information for Business Card
we have 2 address and both should be on the card.
address A: Lindenhoflaan 214B, 3041KP Rotterdam, Tel 010 483 21 95
address B: Zonnewijzerstraat 238, 1062RT Amsterdam Tel 020 571 3829
website www.huidpuntzorg.nu, email info@huidpuntzorg.nu
Look and feel
Each slider illustrates characteristics of the customer's brand and the style your logo design should communicate.

```html
<!DOCTYPE html>
<html lang="nl">
<head>
<meta charset="utf-8">
<title>Huidpuntzorg – visitekaartjes</title>
<link rel="stylesheet" href="https://fonts.googleapis.com/css2?family=Open+Sans:wght@400;600&display=swap">
<style>
  :root {
    --blue: #3f8fd0;
    --blue-light: #4aa3dc;
    --blue-deep: #2f76c0;
    --grey: #8a8c90;
    --ink: #1c1c1c;
    --paper: #ffffff;
    --backdrop: #e9eaec;
  }
  * { box-sizing: border-box; margin: 0; padding: 0; }
  html, body { width: 1200px; height: 900px; overflow: hidden; }
  body {
    background: var(--backdrop);
    font-family: "Open Sans", Arial, sans-serif;
    position: relative;
  }
  .card {
    position: absolute;
    width: 620px;
    height: 370px;
    background: var(--paper);
    overflow: hidden;
    box-shadow: 0 6px 18px rgba(0,0,0,0.18);
  }
  .card--rotterdam { left: 60px; top: 60px; }
  .card--amsterdam { left: 520px; top: 470px; }
  .card__wave { position: absolute; inset: 0; width: 100%; height: 100%; }
  .card__text { position: absolute; white-space: nowrap; }

  .phone {
    top: 30px; right: 32px;
    font-size: 30px; color: var(--ink);
    display: flex; align-items: center; gap: 6px;
  }
  .icon { width: 26px; height: 26px; flex: none; }
  .brand { left: 70px; }
  .brand__name {
    font-size: 44px; font-weight: 400; color: var(--blue-deep);
    letter-spacing: 2px;
    display: flex; align-items: center; gap: 14px;
  }
  .brand__dot {
    width: 18px; height: 18px; border-radius: 50%;
    background: var(--blue-deep);
  }
  .brand__tagline {
    margin-top: 4px; margin-left: 32px;
    font-size: 17px; color: var(--grey); letter-spacing: 2.5px;
  }
  .address { font-size: 22px; line-height: 1.25; text-align: right; }
  .line-item {
    display: flex; align-items: center; gap: 4px; font-size: 22px;
  }
  .on-blue { color: var(--paper); }
  .on-white { color: var(--ink); }

  .card--rotterdam .brand { top: 100px; }
  .card--rotterdam .address { right: 32px; top: 228px; }
  .card--rotterdam .email { right: 32px; top: 292px; }
  .card--rotterdam .web { left: 28px; bottom: 20px; }

  .card--amsterdam .brand { left: 110px; top: 105px; }
  .card--amsterdam .address { right: 32px; top: 208px; }
  .card--amsterdam .email { right: 32px; top: 272px; }
  .card--amsterdam .web { left: 180px; bottom: 18px; }
</style>
</head>
<body>

<section class="card card--rotterdam" aria-label="Visitekaartje vestiging Rotterdam">
  <svg class="card__wave" viewBox="0 0 620 370" preserveAspectRatio="none" aria-hidden="true">
    <defs>
      <linearGradient id="waveBlueA" x1="0" y1="0" x2="1" y2="0">
        <stop offset="0" stop-color="#3479c4"/>
        <stop offset="1" stop-color="#4aa6de"/>
      </linearGradient>
    </defs>
    <path d="M0,262 C120,330 250,300 350,230 C430,175 530,150 620,160 L620,370 L0,370 Z" fill="var(--grey)"/>
    <path d="M0,276 C120,344 250,314 350,244 C430,189 530,164 620,174 L620,370 L0,370 Z" fill="url(#waveBlueA)"/>
  </svg>

  <p class="card__text phone">
    <svg class="icon" viewBox="0 0 24 24" aria-hidden="true"><path fill="var(--ink)" d="M6.6 10.8a15.1 15.1 0 0 0 6.6 6.6l2.2-2.2c.3-.3.7-.4 1-.2 1.1.4 2.3.6 3.6.6.6 0 1 .4 1 1V20c0 .6-.4 1-1 1A17 17 0 0 1 3 4c0-.6.4-1 1-1h3.5c.6 0 1 .4 1 1 0 1.3.2 2.5.6 3.6.1.3 0 .7-.2 1z"/></svg>
    : 010 483 21 95
  </p>

  <div class="card__text brand">
    <p class="brand__name"><span class="brand__dot"></span>HUIDPUNTZORG</p>
    <p class="brand__tagline">next generation skin care</p>
  </div>

  <p class="card__text address on-blue">Lindenhoflaan 214B,<br>3041KP Rotterdam</p>
  <p class="card__text line-item email on-blue">
    <svg class="icon" viewBox="0 0 24 24" aria-hidden="true"><rect x="2.5" y="5.5" width="19" height="13" fill="none" stroke="#fff" stroke-width="1.6"/><path d="M2.5 5.5 12 13l9.5-7.5" fill="none" stroke="#fff" stroke-width="1.6"/></svg>
    : info@huidpuntzorg.nu
  </p>
  <p class="card__text line-item web on-blue">
    <svg class="icon" viewBox="0 0 24 24" aria-hidden="true"><circle cx="12" cy="12" r="10" fill="#fff"/><path d="M2 12h20M12 2c3 3 3 17 0 20M12 2c-3 3-3 17 0 20" fill="none" stroke="var(--blue)" stroke-width="1.2"/></svg>
    : www.huidpuntzorg.nu
  </p>
</section>

<section class="card card--amsterdam" aria-label="Visitekaartje vestiging Amsterdam">
  <svg class="card__wave" viewBox="0 0 620 370" preserveAspectRatio="none" aria-hidden="true">
    <defs>
      <linearGradient id="waveBlueB" x1="0" y1="0" x2="0" y2="1">
        <stop offset="0" stop-color="#3479c4"/>
        <stop offset="1" stop-color="#4aa6de"/>
      </linearGradient>
    </defs>
    <path d="M0,150 C70,205 150,285 168,370 L0,370 Z" fill="var(--grey)"/>
    <path d="M0,162 C62,215 136,292 152,370 L0,370 Z" fill="url(#waveBlueB)"/>
  </svg>

  <p class="card__text phone">
    <svg class="icon" viewBox="0 0 24 24" aria-hidden="true"><path fill="var(--ink)" d="M6.6 10.8a15.1 15.1 0 0 0 6.6 6.6l2.2-2.2c.3-.3.7-.4 1-.2 1.1.4 2.3.6 3.6.6.6 0 1 .4 1 1V20c0 .6-.4 1-1 1A17 17 0 0 1 3 4c0-.6.4-1 1-1h3.5c.6 0 1 .4 1 1 0 1.3.2 2.5.6 3.6.1.3 0 .7-.2 1z"/></svg>
    : 020 571 3829
  </p>

  <div class="card__text brand">
    <p class="brand__name"><span class="brand__dot"></span>HUIDPUNTZORG</p>
    <p class="brand__tagline">next generation skin care</p>
  </div>

  <p class="card__text address on-white">Zonnewijzerstraat 238,<br>1062RT Amsterdam</p>
  <p class="card__text line-item email on-white">
    <svg class="icon" viewBox="0 0 24 24" aria-hidden="true"><rect x="2.5" y="5.5" width="19" height="13" fill="none" stroke="var(--ink)" stroke-width="1.6"/><path d="M2.5 5.5 12 13l9.5-7.5" fill="none" stroke="var(--ink)" stroke-width="1.6"/></svg>
    : info@huidpuntzorg.nu
  </p>
  <p class="card__text line-item web on-white">
    <svg class="icon" viewBox="0 0 24 24" aria-hidden="true"><circle cx="12" cy="12" r="10" fill="var(--ink)"/><path d="M2 12h20M12 2c3 3 3 17 0 20M12 2c-3 3-3 17 0 20" fill="none" stroke="#fff" stroke-width="1.2"/></svg>
    : www.huidpuntzorg.nu
  </p>
</section>

</body>
</html>
```